Brimvale OralNet IT Inc. new website

i need a website for my company which is dedicated to installation and service of computer systems in Dental Offices. I would like for it to encompass a technology feel and professional look. The company deals with all aspects of technology like, Audio Visual, computer systems and networks, Cloud services like data backup, data center. We provide manage services, support and services to Dental Professionals.

Looking for a Technology font but professional look Added Wednesday, April 20, 2016

Target Market(s)

Dental, Dentist

Industry/Entity Type

Dental

Number of Pages Required

5+ page

Font styles to use
Other font styles liked:
• Futuristic or Techy

Colors
0255a3
ec1f27

Requirements
Must have
• Tabs
Nice to have
• Have no idea maybe some suggestion on your part may help
Should not have
• A professional feel but have a techy look

```html
<!DOCTYPE html>
<html lang="en">
<head>
<meta charset="utf-8">
<title>Brimvale OralNet IT Inc.</title>
<link href="https://fonts.googleapis.com/css2?family=Roboto+Slab:wght@400;700&family=Open+Sans:wght@400;600;700&display=swap" rel="stylesheet">
<style>
:root{
  --blue:#0255a3;
  --red:#ec1f27;
  --red-soft:#ef5157;
  --ink:#222;
  --text:#666;
  --muted:#999;
  --line:#e8e8e8;
  --grey-bg:#f2f2f2;
  --footer:#222222;
  --footer-deep:#1a1a1a;
  --white:#fff;
}
*{margin:0;padding:0;box-sizing:border-box}
html,body{width:1200px;height:4215px;overflow:hidden}
body{font-family:"Open Sans",Arial,sans-serif;color:var(--text);background:var(--white);position:relative}
.slab{font-family:"Roboto Slab",Georgia,serif}
.abs{position:absolute}
section{position:absolute;left:0;width:1200px}

/* top bar */
.topbar{top:0;height:22px;background:var(--blue);color:var(--white);font-size:10px;display:flex;justify-content:flex-end;align-items:center;gap:14px;padding-right:225px}
.topbar .dots{display:flex;gap:6px}
.topbar .dots span{width:9px;height:9px;border-radius:50%;background:rgba(255,255,255,.85)}

/* header */
.header{top:22px;height:62px;background:var(--white);border-bottom:1px solid var(--line)}
.brand{left:205px;top:12px;display:flex;align-items:center;gap:8px;font-family:"Open Sans",sans-serif;font-weight:700;font-size:17px;color:var(--blue);line-height:1.05}
.brand .mark{width:30px;height:30px;background:var(--blue)}
.brand small{display:block;font-size:17px}
.nav{left:441px;top:0;height:62px;display:flex;align-items:center;gap:26px;font-size:11px;font-weight:600;color:#333;letter-spacing:.3px}
.nav .active{color:var(--red);position:relative}
.nav .active::after{content:"";position:absolute;left:0;right:0;bottom:-22px;height:2px;background:var(--red)}

/* hero */
.hero{top:84px;height:413px;background:linear-gradient(100deg,#cfd6da 0%,#e9ecec 30%,#9fbcb8 55%,#e6e8e6 80%,#c8cccd 100%)}
.dedicated{left:225px;top:352px;width:750px;height:34px;background:#1e2a33;color:#fff;text-align:center;font-size:17px;line-height:34px;font-family:"Roboto Slab",serif}
.tabs{left:225px;top:470px;width:750px;height:157px;display:flex}
.tab{flex:1;color:#fff;text-align:center;padding-top:16px}
.tab .ic{width:44px;height:44px;border-radius:50%;background:rgba(255,255,255,.25);margin:0 auto 10px;display:flex;align-items:center;justify-content:center}
.tab h3{font-family:"Roboto Slab",serif;font-size:22px;font-weight:700}
.tab p{font-size:10px;margin-top:6px;opacity:.9}
.t1{background:var(--blue)}.t2{background:var(--red)}.t3{background:var(--red-soft)}

/* section headings */
.eyebrow{width:1200px;text-align:center;font-size:12px;letter-spacing:1.5px;color:var(--muted);text-transform:uppercase}
.title{width:1200px;text-align:center;font-family:"Roboto Slab",serif;font-weight:700;font-size:24px;color:var(--ink)}

/* about */
.feature{width:250px;text-align:center}
.feature svg{display:block;margin:0 auto}
.feature h4{font-family:"Open Sans",sans-serif;font-weight:400;font-size:20px;color:#333;margin-top:16px}
.feature p{font-size:11px;line-height:16px;margin:14px auto 0;width:190px}
.more{font-size:10px;color:var(--red);display:block;margin-top:14px}
.rule{left:0;width:1200px;height:1px;background:var(--line)}

/* how it works */
.chart-label{text-align:center;font-size:12px;color:#555;line-height:16px}

/* research */
.research{top:1776px;height:705px;background:var(--grey-bg)}
.lead{left:270px;width:660px;text-align:center;font-size:12px;line-height:17px;color:#666}
.video{left:312px;top:337px;width:576px;height:320px;background:linear-gradient(110deg,#7a2a2c 0%,#a09a92 40%,#d8dee2 65%,#8b95a3 100%)}
.play{left:266px;top:141px;width:46px;height:36px;border-radius:9px;background:var(--red)}

/* team */
.member{width:360px;display:flex;gap:25px}
.avatar{width:101px;height:101px;border-radius:50%;background:linear-gradient(135deg,#c9b7a6,#8a7c70);flex:none}
.member h5{font-family:"Roboto Slab",serif;font-weight:700;font-size:17px;color:var(--blue);margin-top:6px}
.member p{font-size:12px;line-height:16px;margin-top:10px}

/* blog */
.post{width:240px}
.meta{font-size:9px;color:var(--muted);display:flex;justify-content:space-between}
.meta b{color:var(--red);font-weight:400}
.thumb{height:132px;margin-top:10px}
.post h6{font-family:"Roboto Slab",serif;font-weight:700;font-size:17px;color:#333;margin-top:20px}
.post p{font-size:11px;line-height:16px;margin-top:12px}

/* quote */
.quote{top:3540px;height:231px;background:var(--blue);color:#fff;text-align:center}
.quote .eyebrow{color:#fff;position:absolute;top:64px;font-weight:700}
.quote h2{position:absolute;top:96px;width:1200px;font-family:"Roboto Slab",serif;font-size:28px;font-weight:700}
.btn{left:486px;top:158px;width:242px;height:39px;background:var(--red);color:#fff;font-size:12px;line-height:39px;font-weight:600;letter-spacing:.5px}

/* footer */
.footer{top:3771px;height:444px;background:var(--footer);color:#bbb;font-size:11px;line-height:15px}
.footer h4{font-family:"Roboto Slab",serif;font-size:19px;color:#fff;font-weight:700}
.fbrand{font-weight:700;font-size:17px;color:#fff;display:flex;align-items:center;gap:8px;line-height:1.05}
.fbrand .mark{width:26px;height:26px;background:var(--blue)}
.map{width:239px;height:118px;background:linear-gradient(135deg,#e7e3da,#d5dccf 60%,#eae6dd)}
.social{display:flex;gap:6px}
.social span{width:25px;height:25px;border-radius:50%;background:var(--blue)}
.social span:nth-child(3){background:var(--red)}
.menu li{list-style:none;font-size:10px;line-height:16px;color:#aaa}
.bottom{left:0;top:377px;width:1200px;height:67px;background:var(--footer-deep)}
.copy{left:225px;top:26px;font-size:10px;color:#aaa}
.totop{left:989px;top:14px;width:37px;height:37px;background:var(--red)}
</style>
</head>
<body>

<section class="topbar">
  <span>&#9742; (800) 555-0142</span>
  <span>&#9993; info@brimvaleoralnet.com</span>
  <span class="dots"><span></span><span></span><span></span><span></span></span>
</section>

<section class="header">
  <div class="brand abs"><span class="mark"></span><span>Brimvale<small>OralNet IT</small></span></div>
  <nav class="nav abs">
    <span class="active">HOME</span><span>ABOUT US</span><span>SERVICES</span><span>TECHNOLOGY</span><span>RESEARCH</span><span>NEWS</span><span>CONTACT US</span>
    <svg width="14" height="14" viewBox="0 0 14 14"><circle cx="6" cy="6" r="4.5" fill="none" stroke="#333" stroke-width="1.8"/><line x1="9.3" y1="9.3" x2="13" y2="13" stroke="#333" stroke-width="2"/></svg>
  </nav>
</section>

<section class="hero" role="img" aria-label="Photo of a dental team treating a patient in a modern clinic"></section>
<div class="dedicated abs">We are Dedicated to</div>
<div class="tabs abs">
  <div class="tab t1"><div class="ic"><svg width="22" height="22" viewBox="0 0 22 22"><rect x="4" y="7" width="14" height="9" rx="1" fill="none" stroke="#fff" stroke-width="2"/><path d="M8 7V4h6v3" fill="none" stroke="#fff" stroke-width="2"/></svg></div><h3>Install</h3><p>Neque porro quisquam est qui sit amet...</p></div>
  <div class="tab t2"><div class="ic"><svg width="22" height="22" viewBox="0 0 22 22"><circle cx="11" cy="5" r="3" fill="#fff"/><circle cx="5" cy="16" r="3" fill="#fff"/><circle cx="17" cy="16" r="3" fill="#fff"/><path d="M11 8v4M11 12L6 14M11 12l5 2" stroke="#fff" stroke-width="1.5"/></svg></div><h3>Manage</h3><p>Duis autem vel eum iure reprehenderit...</p></div>
  <div class="tab t3"><div class="ic"><svg width="22" height="22" viewBox="0 0 22 22"><path d="M4 18L15 7M7 4l11 11" stroke="#fff" stroke-width="2.5" stroke-linecap="round"/></svg></div><h3>Support</h3><p>Vel illum qui dolorem eum fugiat quo...</p></div>
</div>

<!-- about -->
<div class="eyebrow abs" style="top:675px">About Us</div>
<div class="title abs" style="top:700px">We Are the Trusted Experts</div>
<div class="feature abs" style="left:180px;top:818px">
  <svg width="56" height="50" viewBox="0 0 56 50"><path d="M6 18h10l14-12v38L16 32H6z" fill="none" stroke="var(--blue)" stroke-width="2.5"/><path d="M36 17a10 10 0 0 1 0 16M41 11a18 18 0 0 1 0 28" fill="none" stroke="var(--blue)" stroke-width="2.5"/></svg>
  <h4>Audio Visual</h4>
  <p>Duis aute irure dolor in; voluptate velit esse cillum dolore eu fugiat nulla pariatur.</p>
  <span class="more">Learn More</span>
</div>
<div class="feature abs" style="left:475px;top:818px">
  <svg width="60" height="50" viewBox="0 0 60 50"><rect x="22" y="3" width="16" height="11" fill="none" stroke="var(--blue)" stroke-width="2.5"/><rect x="3" y="36" width="14" height="11" fill="none" stroke="var(--blue)" stroke-width="2.5"/><rect x="23" y="36" width="14" height="11" fill="none" stroke="var(--blue)" stroke-width="2.5"/><rect x="43" y="36" width="14" height="11" fill="none" stroke="var(--blue)" stroke-width="2.5"/><path d="M30 14v22M10 36v-10h40v10" fill="none" stroke="var(--blue)" stroke-width="2.5"/></svg>
  <h4>Systems &amp; Networks</h4>
  <p>Cupidatat non proident, sunt in culpa qui officia deserunt mollit anim id est laborum.</p>
  <span class="more">Learn More</span>
</div>
<div class="feature abs" style="left:770px;top:818px">
  <svg width="60" height="50" viewBox="0 0 60 50"><path d="M16 34H12a9 9 0 0 1 0-18 13 13 0 0 1 25-4 10 10 0 0 1 12 11 6 6 0 0 1-1 11H44" fill="none" stroke="var(--blue)" stroke-width="2.5"/><path d="M30 22v24M23 39l7 7 7-7" fill="none" stroke="var(--blue)" stroke-width="2.5"/></svg>
  <h4>Cloud Services</h4>
  <p>Reiciendis voluptatibus maiores alias consequatur aut perferendis doloribus asperiores.</p>
  <span class="more">Learn More</span>
</div>
<div class="rule abs" style="top:1062px"></div>

<!-- how it works -->
<div class="eyebrow abs" style="top:1110px">What We Do</div>
<div class="title abs" style="top:1135px">How It Works</div>
<svg class="abs" style="left:300px;top:1200px" width="600" height="520" viewBox="0 0 600 520" aria-label="Service cycle chart">
  <g fill="none" stroke-width="12" transform="rotate(-90 296 247)">
    <circle cx="296" cy="247" r="175" stroke="var(--blue)" stroke-dasharray="660 1100"/>
    <circle cx="296" cy="247" r="156" stroke="var(--red)" stroke-dasharray="0 250 800 1000"/>
    <circle cx="296" cy="247" r="137" stroke="var(--blue)" stroke-dasharray="560 900"/>
    <circle cx="296" cy="247" r="118" stroke="var(--red)" stroke-dasharray="0 60 680 800"/>
  </g>
  <circle cx="296" cy="247" r="100" fill="#fff"/>
  <text x="296" y="253" text-anchor="middle" font-family="Open Sans,sans-serif" font-weight="700" font-size="17" fill="#b9c9dc">Brimvale</text>
  <path d="M225 75L200 60M455 170L540 150M150 320L90 340M296 420V470" stroke="#ccc" stroke-width="1.5" fill="none"/>
  <g stroke="var(--red)" fill="none" stroke-width="2"><circle cx="200" cy="38" r="7"/><path d="M194 48l-4 8M206 48l4 8"/></g>
  <g stroke="var(--blue)" fill="none" stroke-width="2"><circle cx="580" cy="135" r="8"/><path d="M580 120v30M565 135h30"/></g>
  <g stroke="var(--blue)" fill="none" stroke-width="2"><rect x="49" y="276" width="14" height="18"/><rect x="55" y="270" width="14" height="18"/></g>
  <g stroke="var(--red)" fill="none" stroke-width="2"><circle cx="296" cy="479" r="7"/><path d="M293 488h6v5h-6z"/></g>
</svg>
<div class="chart-label abs" style="left:440px;top:1258px;width:120px">Support</div>
<div class="chart-label abs" style="left:820px;top:1363px;width:120px">Install</div>
<div class="chart-label abs" style="left:277px;top:1510px;width:160px">Cloud services of<br>data backup</div>
<div class="chart-label abs" style="left:516px;top:1709px;width:160px">Manage Services</div>

<!-- research -->
<section class="research">
  <div class="eyebrow abs" style="top:52px">Research Areas</div>
  <div class="title abs" style="top:82px">We Deliver Innovative Solutions</div>
  <p class="lead abs" style="top:150px">Temporibus autem quibusdam et aut officiis debitis aut rerum necessitatibus saepe eveniet ut et voluptates repudiandae sint et molestiae non recusandae. Itaque earum rerum hic tenetur a sapiente delectus, ut aut reiciendis voluptatibus maiores alias consequatur aut perferendis doloribus asperiores repellat. Quo blanditiis praesentium voluptatum deleniti atque corrupti quos dolores et quas molestias excepturi sint occaecati cupiditate non provident, similique sunt in culpa qui officia deserunt mollitia animi, id est laborum et dolorum fuga. Et harum quidem rerum facilis est et expedita distinctio. Nam libero tempore, cum soluta nobis est eligendi optio cumque nihil impedit quo minus id quod maxime placeat facere possimus omnis voluptas assumenda est omnis dolor repellendus.</p>
  <div class="video abs" role="img" aria-label="Video still of two technicians working at dental imaging equipment">
    <div class="play abs"><svg width="46" height="36" viewBox="0 0 46 36"><path d="M18 11l11 7-11 7z" fill="#fff"/></svg></div>
  </div>
</section>

<!-- team -->
<div class="eyebrow abs" style="top:2532px">Meet the Team</div>
<div class="title abs" style="top:2557px">They Have Wide Range of Experience</div>
<div class="member abs" style="left:225px;top:2656px"><div class="avatar" role="img" aria-label="Portrait of Owen Marsh"></div><div><h5>Owen Marsh</h5><p>Duis aute irure dolor in reprehenderit in voluptate velit esse cillum dolore eu fugiat nulla pariatur. Excepteur sint occaecat cupidatat non proident.</p></div></div>
<div class="member abs" style="left:613px;top:2656px"><div class="avatar" role="img" aria-label="Portrait of Clara Fenwick"></div><div><h5>Clara Fenwick</h5><p>Temporibus autem quibusdam et aut officiis debitis aut rerum necessitatibus saepe eveniet ut et voluptates sint et molestiae non recusandae.</p></div></div>
<div class="member abs" style="left:225px;top:2822px"><div class="avatar" role="img" aria-label="Portrait of Mira Dalton"></div><div><h5>Mira Dalton</h5><p>Itaque earum rerum hic tenetur a sapiente delectus, ut aut reiciendis voluptatibus maiores alias aut perferendis dolor.</p></div></div>
<div class="member abs" style="left:613px;top:2822px"><div class="avatar" role="img" aria-label="Portrait of Peter Lindqvist"></div><div><h5>Peter Lindqvist</h5><p>Nemo enim ipsam voluptatem quia voluptas sit aspernatur aut odit aut fugit, sed quia consequuntur magni dolores eos qui ratione.</p></div></div>
<div class="rule abs" style="top:3021px"></div>

<!-- blog -->
<div class="eyebrow abs" style="top:3056px">From the Blog</div>
<div class="title abs" style="top:3080px">Learn About Our Leading Technologies</div>
<div class="post abs" style="left:225px;top:3172px">
  <div class="meta"><span>Posted April 21, 2016</span><b>&#9679; 18 &nbsp; &#9675; 11</b></div>
  <div class="thumb" role="img" aria-label="Photo of a technician servicing computer hardware" style="background:linear-gradient(120deg,#c7a57a,#6b5b4c 60%,#a9a9a9)"></div>
  <h6>Qui Officia Deserunt...</h6>
  <p>Quis autem vel eum iure qui in ea velit esse quam nihil molestiae consequatur vel illum qui dolorem eum fugiat quo voluptas nulla pariatur.</p>
  <span class="more">Read More</span>
</div>
<div class="post abs" style="left:483px;top:3172px">
  <div class="meta"><span>Posted April 21, 2016</span><b>&#9679; 18 &nbsp; &#9675; 5</b></div>
  <div class="thumb" role="img" aria-label="Photo of a row of networked computer workstations" style="background:linear-gradient(120deg,#2d6f8e,#8fc4d6 50%,#3c7d98)"></div>
  <h6>Luis Nostrud Ullamco...</h6>
  <p>Occaecati cupiditate non provident sunt in culpa qui officia deserunt mollitia animi, id est laborum et dolorum fuga et expedita.</p>
  <span class="more">Read More</span>
</div>
<div class="post abs" style="left:739px;top:3172px">
  <div class="meta"><span>Posted April 19, 2016</span><b>&#9679; 18 &nbsp; &#9675; 9</b></div>
  <div class="thumb" role="img" aria-label="Photo of a presenter showing a slide to a small team" style="background:linear-gradient(120deg,#b9a792,#e1dcd2 50%,#7d8c99)"></div>
  <h6>Qui Officia Deserunt...</h6>
  <p>Sed quia non numquam eius modi tempora incidunt ut labore et dolore magnam aliquam quaerat voluptatem ullam corporis suscipit.</p>
  <span class="more">Read More</span>
</div>

<!-- quotations -->
<section class="quote">
  <div class="eyebrow">Quotations</div>
  <h2>Your Request Answered Within 24 Hours</h2>
  <div class="btn abs">DOWNLOAD THE FORM</div>
</section>

<!-- footer -->
<section class="footer">
  <div class="fbrand abs" style="left:225px;top:60px"><span class="mark"></span><span>Brimvale<br>OralNet IT</span></div>
  <p class="abs" style="left:225px;top:125px;width:240px">Lorem ipsum dolor sit amet, consectetur adipiscing elit, sed do eiusmod tempor incididunt ut labore et dolore magna aliqua. Ut enim ad minim veniam.</p>
  <div class="map abs" style="left:225px;top:214px" role="img" aria-label="Street map showing the office location"></div>
  <h4 class="abs" style="left:565px;top:56px">Contact Us</h4>
  <p class="abs" style="left:565px;top:110px;width:220px">418 Kestrel Way,<br>Brimvale, IL 60990<br>info@brimvaleoralnet.com<br><br>Tel: (800) 555-0142<br>Fax: (800) 555-0199</p>
  <h4 class="abs" style="left:823px;top:56px">Follow Us</h4>
  <div class="social abs" style="left:823px;top:106px"><span></span><span></span><span></span><span></span></div>
  <h4 class="abs" style="left:823px;top:168px">Menu</h4>
  <ul class="menu abs" style="left:823px;top:218px"><li>Home</li><li>About Us</li><li>Services</li><li>Research</li><li>Contact Us</li><li>News</li></ul>
  <div class="bottom abs">
    <div class="copy abs">&copy; Copyright information here</div>
    <div class="totop abs"><svg width="37" height="37" viewBox="0 0 37 37"><path d="M13 21l5.5-5.5L24 21" fill="none" stroke="#fff" stroke-width="2"/></svg></div>
  </div>
</section>

</body>
</html>
```